Trade Show Booth Sign Design for Retracting Banner

I need a trade show booth sign designed. It will be for a retractable banner that is double sided with 34 by 81 inch.

I want to incorporate my logo (see attached, have it in other file formats as well) and graphics from my website (https://www.dolbrookteachingadvisory.com/) with parts or all of the following text.

· Educational Content Creation
o Supplemental Textbook Content Development
o E-learning Content Development
· Curriculum Development
o KVTR/Bright Ladder
o Three Dimensional Learning
· Assessment
o Formative Assessments
o Elementary School, Middle School, High School, College, and Business
· Professional Development
o Training
o Facilitation

Target Market(s)

Education

Industry/Entity Type

Education

Font styles to use
Sans Serif

Colors

Designer to choose colors to be used in the design.

Requirements
Must have
• Eye catching and easy to read design
Nice to have
• Would like to see incorporation of my logo and some of the elements of my website images
Should not have
• N/A

```html
<!DOCTYPE html>
<html lang="en">
<head>
<meta charset="utf-8">
<title>Dolbrook Teaching Advisory – Retractable Banner</title>
<link rel="stylesheet" href="https://fonts.googleapis.com/css2?family=Nunito:wght@300;700;800;900&display=swap">
<style>
  :root {
    --page-bg: #ececec;
    --header-charcoal: #333335;
    --banner-white: #ffffff;
    --navy-deep: #161c48;
    --navy-mid: #1f2a63;
    --navy-soft: #2e3b7d;
    --navy-icon: #1b2458;
    --icon-glow: #35468f;
    --text-white: #ffffff;
    --text-muted: #d6d9ea;
    --photo-teal: #5d8592;
    --photo-wood: #b48a62;
    --photo-skin: #d2ad92;
    --photo-dark: #2b2f3a;
  }
  * { box-sizing: border-box; margin: 0; padding: 0; }
  html, body {
    width: 1200px;
    height: 1090px;
    overflow: hidden;
    background: var(--page-bg);
    font-family: "Nunito", sans-serif;
  }
  .banner {
    position: absolute;
    left: 375px;
    top: 15px;
    width: 450px;
    height: 1060px;
    background: var(--banner-white);
    overflow: hidden;
  }
  .brand-header {
    position: absolute;
    left: 0; top: 0;
    width: 100%;
    height: 138px;
    background: var(--header-charcoal);
    color: var(--text-white);
    text-align: center;
    padding-top: 16px;
  }
  .brand-name {
    font-weight: 900;
    font-size: 68px;
    line-height: 72px;
    letter-spacing: 1px;
  }
  .brand-tagline {
    font-weight: 900;
    font-size: 26px;
    line-height: 30px;
  }
  .hero-photo {
    position: absolute;
    left: 0; top: 157px;
    width: 100%;
    height: 269px;
    background:
      radial-gradient(ellipse 30% 45% at 82% 45%, var(--photo-skin) 0%, transparent 70%),
      radial-gradient(ellipse 25% 40% at 45% 50%, #c7a58e 0%, transparent 70%),
      radial-gradient(ellipse 20% 35% at 12% 55%, var(--photo-dark) 0%, transparent 75%),
      linear-gradient(180deg, var(--photo-teal) 0%, #7c8f95 45%, var(--photo-wood) 78%, #8c6a52 100%);
  }
  .services-panel {
    position: absolute;
    left: 0; top: 446px;
    width: 100%;
    height: 614px;
    background:
      radial-gradient(ellipse 40% 30% at 80% 72%, rgba(70,85,160,0.45) 0%, transparent 70%),
      linear-gradient(180deg, transparent 0%, transparent 72%, rgba(80,95,170,0.35) 80%, rgba(40,52,115,0.6) 90%, transparent 100%),
      linear-gradient(180deg, var(--navy-deep) 0%, var(--navy-mid) 55%, var(--navy-soft) 100%);
  }
  .service-icon {
    position: absolute;
    left: 20px;
    width: 102px;
    height: 102px;
    border-radius: 50%;
    border: 6px solid var(--banner-white);
    background: radial-gradient(circle at 50% 45%, var(--icon-glow) 0%, var(--navy-icon) 70%);
    box-shadow: 0 0 0 2px var(--navy-deep), 0 2px 6px rgba(0,0,0,0.4);
  }
  .service {
    position: absolute;
    left: 140px;
    width: 300px;
    color: var(--text-white);
  }
  .service-title {
    font-weight: 700;
    font-size: 23.5px;
    line-height: 29px;
  }
  .service-item {
    font-weight: 300;
    font-size: 16px;
    line-height: 20px;
    color: var(--text-muted);
    margin-top: 4px;
  }
  .service-title + .service-item { margin-top: 6px; }
</style>
</head>
<body>
  <main class="banner">
    <header class="brand-header">
      <div class="brand-name">DOLBROOK</div>
      <div class="brand-tagline">Teaching Advisory</div>
    </header>

    <div class="hero-photo" role="img" aria-label="Photo of students writing together at a classroom table"></div>

    <section class="services-panel" role="img" aria-label="Faint navy-tinted photo of a hand writing in a spiral notebook"></section>

    <div class="service-icon" style="top:466px" role="img" aria-label="Icon of a head with a light bulb and ideas"></div>
    <div class="service" style="top:474px">
      <h2 class="service-title">Educational Content<br>Creation</h2>
      <p class="service-item">Supplemental Textbook Content Development</p>
      <p class="service-item">E-learning Content Development</p>
    </div>

    <div class="service-icon" style="top:585px" role="img" aria-label="Icon of a teacher presenting a chart to a class"></div>
    <div class="service" style="top:605px">
      <h2 class="service-title">Curriculum Development</h2>
      <p class="service-item">KVTR/Bright Ladder</p>
      <p class="service-item">Three Dimensional Learning</p>
    </div>

    <div class="service-icon" style="top:702px" role="img" aria-label="Icon of a flask surrounded by science symbols"></div>
    <div class="service" style="top:685px">
      <h2 class="service-title">Assessment</h2>
      <p class="service-item">Formative Assessments</p>
      <p class="service-item">Elementary School, Middle School, High School, College, and Business</p>
    </div>

    <div class="service-icon" style="top:820px" role="img" aria-label="Icon of a trainer presenting to a group"></div>
    <div class="service" style="top:792px">
      <h2 class="service-title">Professional<br>Development</h2>
      <p class="service-item">Training</p>
      <p class="service-item">Facilitation</p>
    </div>
  </main>
</body>
</html>
```